Tiroler party ecommerce site

We have a eCommerce site that needs a redesign. What we need are 3 pages: a frontpage, a product listing page and a product page.

The look has to be:
fun, modern, fresh, bright, professional look but not corporate.

Some content keywords are :
Carnival, oktoberfesten, tirol, dirndl, leder hosen, beer, women with big breast (no porn! just fun)

Some functional hints :

The frontpage needs to give a good impression of all the products on the site.
There should also be some space for campaigns or banners on the frontpage.

The product listing page should have facets (search options) and a search field.

The product page should have a few boxes such as related products, others viewed, comments etc.. (your average product page content)

All pages should show a small cart button or box and off course a kick ass menu!

Some links :

The current site http://www.feestkraamwinkel.nl/

We couldn't find any site to show as inspiration most party sites are very bad!.

```html
<!DOCTYPE html>
<html lang="en">
<head>
<meta charset="utf-8">
<title>Alpenfeest – Trioolse Dames</title>
<link href="https://fonts.googleapis.com/css2?family=Arvo:wght@400;700&family=Open+Sans:wght@400;600;700&display=swap" rel="stylesheet">
<style>
:root{
  --bg:#f1e8d2;
  --topbar:#3a170b;
  --orange:#f04e23;
  --white:#ffffff;
  --nav:#f6efe0;
  --text:#3b2a1e;
  --muted:#6b5a48;
  --blue:#45b5e0;
  --brown-banner:#c48a4b;
  --red-banner:#e9472a;
  --yellow-banner:#f3b81d;
  --footer:#c99a5b;
  --footer-bottom:#a87a3f;
  --line:#e3d8c2;
}
*{box-sizing:border-box;margin:0;padding:0}
html,body{width:1200px;height:2527px;overflow:hidden}
body{background:var(--bg);font-family:"Open Sans",Arial,sans-serif;color:var(--text);position:relative}
a{color:inherit;text-decoration:none}
ul{list-style:none}

.topbar{height:29px;background:var(--topbar);color:var(--white);font-size:12px;display:flex;align-items:center;padding:0 94px;justify-content:space-between}
.topbar .links{display:flex;height:100%}
.topbar .links a{display:flex;align-items:center;padding:0 14px;height:100%}
.topbar .links a.active{background:var(--orange)}
.topbar .account{display:flex;gap:40px;align-items:center}
.topbar .account span{display:flex;align-items:center;gap:6px}

.header{height:104px;background:var(--white);display:flex;align-items:center;padding:0 88px;justify-content:space-between}
.brand{font-family:"Arvo",Georgia,serif;font-weight:700;font-size:30px;color:var(--topbar);letter-spacing:1px;display:flex;align-items:center;gap:10px}
.brand .mark{width:14px;height:14px;background:var(--orange)}
.search{display:flex;margin-left:260px}
.search input{width:270px;height:38px;border:1px solid var(--line);padding:0 12px;font:13px "Open Sans",sans-serif;color:var(--muted)}
.search button{width:40px;height:38px;background:var(--orange);border:0;display:flex;align-items:center;justify-content:center}
.cart{margin-left:auto;background:var(--topbar);color:var(--white);height:40px;width:136px;display:flex;align-items:center;justify-content:space-between;padding:0 6px 0 12px;font-size:14px;font-weight:600}
.cart .count{background:var(--orange);width:26px;height:26px;display:flex;align-items:center;justify-content:center}

.mainnav{height:56px;background:var(--nav);display:flex;align-items:center;padding:0 76px;gap:58px;font-size:15px;color:var(--text)}
.mainnav a::after{content:"";display:inline-block;margin-left:8px;border:5px solid transparent;border-top-color:var(--text);vertical-align:-1px}
.mainnav a.plain::after{display:none}

.page{display:flex;padding:53px 0 0 71px}
.facets{width:268px;font-size:15px}
.facets h3{font-family:"Arvo",Georgia,serif;font-size:18px;margin-bottom:18px}
.facets ul{margin-bottom:58px;line-height:22px}
.facets li.active{color:var(--orange)}

.content{width:740px}
.breadcrumb{font-size:16px;margin-bottom:40px}
.title{font-family:"Arvo",Georgia,serif;font-size:34px;letter-spacing:3px;font-weight:700;margin-bottom:22px}
.intro{font-size:16px;line-height:23px;color:var(--muted);margin-bottom:30px;width:730px}
.products{display:grid;grid-template-columns:repeat(3,232px);column-gap:20px;row-gap:52px}
.card{background:var(--white);height:326px;box-shadow:0 1px 3px rgba(0,0,0,.08)}
.card .photo{height:230px;margin:0 6px;border-bottom:1px solid var(--line)}
.photo.hat{background:linear-gradient(#f7f4ee 0%,#4f7a3a 35%,#7a5236 75%,#5a3b24)}
.photo.pants{background:linear-gradient(#f6f1ea 0%,#c9a3ac 30%,#b48b8e 60%,#6e5744)}
.photo.wig{background:linear-gradient(#f7efe6 0%,#e2512a 35%,#8ec44c 55%,#d84a35)}
.card .name{font-size:14px;padding:12px 12px 0}
.card .row{display:flex;justify-content:space-between;align-items:center;padding:20px 12px 0}
.card .price{font-size:18px}
.card .buy{background:var(--blue);color:var(--white);font-size:9px;font-weight:700;padding:5px 0;width:88px;text-align:center}

.banners{position:absolute;top:1627px;left:94px;display:flex;gap:17px}
.banner{width:319px;height:183px;padding:20px 18px;color:var(--white);display:flex;justify-content:space-between}
.banner.new{background:var(--brown-banner)}
.banner.hot{background:var(--red-banner)}
.banner.sale{background:var(--yellow-banner)}
.banner h4{font-family:"Arvo",Georgia,serif;font-size:44px;font-weight:700;line-height:1}
.banner p{font-size:12px;font-weight:600;width:150px;margin:12px 0 18px;line-height:17px}
.banner .view{background:var(--blue);font-size:9px;font-weight:700;padding:7px 18px;display:inline-block}
.banner .art{width:110px;height:145px;border-radius:6px}
.new .art{background:linear-gradient(#b78247,#7c5a3a)}
.hot .art{background:linear-gradient(#e9472a,#6a4a3a)}
.sale .art{background:linear-gradient(#f3b81d,#8a4a3a)}

.signup{position:absolute;top:1863px;left:91px;width:979px;height:257px;background:var(--white);text-align:center;padding-top:34px}
.signup h2{font-family:"Arvo",Georgia,serif;font-size:26px;letter-spacing:1px;margin-bottom:10px}
.signup p{font-size:15px;line-height:26px;width:500px;margin:0 auto 22px}
.signup input{display:block;margin:0 auto 12px;width:282px;height:44px;border:1px solid var(--line);text-align:center;font:13px "Open Sans",sans-serif;color:var(--muted)}
.signup button{width:282px;height:44px;background:var(--orange);border:0;color:var(--white);font:600 14px "Open Sans",sans-serif}

.footer{position:absolute;top:2176px;left:0;width:1200px;height:259px;background:var(--footer);color:var(--white);display:flex;padding:28px 0 0 99px;gap:0}
.footer section{width:370px}
.footer h5{font-size:18px;font-weight:600;margin-bottom:34px}
.footer li{font-size:16px;line-height:23px}
.social{display:flex;gap:11px}
.social span{width:34px;height:34px;border:2px solid rgba(255,255,255,.8)}
.bottombar{position:absolute;top:2435px;left:0;width:1200px;height:92px;background:var(--footer-bottom);color:var(--white);text-align:center;padding-top:18px;font-size:14px}
.payments{display:flex;gap:8px;justify-content:center;margin-top:14px}
.payments span{width:42px;height:28px;background:var(--white);border-radius:3px}
.payments span.wide{width:80px;background:none;border:2px solid var(--white)}
</style>
</head>
<body>
<div class="topbar">
  <nav class="links"><a class="active">About</a><a>Information ▾</a><a>Contact</a></nav>
  <div class="account">
    <span><svg width="13" height="13" viewBox="0 0 24 24"><path fill="#fff" d="M6.6 10.8a15 15 0 006.6 6.6l2.2-2.2c.3-.3.7-.4 1-.2 1.1.4 2.3.6 3.6.6.6 0 1 .4 1 1V20c0 .6-.4 1-1 1A17 17 0 013 4c0-.6.4-1 1-1h3.5c.6 0 1 .4 1 1 0 1.3.2 2.5.6 3.6.1.3 0 .7-.2 1z"/></svg>074 555 01 23</span>
    <span><svg width="12" height="12" viewBox="0 0 24 24"><circle cx="12" cy="7" r="5" fill="#fff"/><path fill="#fff" d="M2 23c0-6 4.5-9 10-9s10 3 10 9z"/></svg>Login / Register</span>
  </div>
</div>

<header class="header">
  <div class="brand">ALPENFEEST<span class="mark"></span></div>
  <form class="search"><input value="What are you looking for ?"><button type="button"><svg width="16" height="16" viewBox="0 0 24 24"><circle cx="10" cy="10" r="7" fill="none" stroke="#fff" stroke-width="3"/><path d="M15 15l7 7" stroke="#fff" stroke-width="3"/></svg></button></form>
  <div class="cart"><svg width="20" height="16" viewBox="0 0 24 20"><path d="M1 2h4l3 11h12l3-8H7" fill="none" stroke="#fff" stroke-width="2"/><circle cx="10" cy="17" r="2" fill="#fff"/><circle cx="19" cy="17" r="2" fill="#fff"/></svg>Cart ▾<span class="count">0</span></div>
</header>

<nav class="mainnav">
  <a>Tiroler Kleding</a><a>Kleding Accessories</a><a class="plain">Tiroler Schorten</a><a>Tiroler Hoeden</a><a>Decoraties</a><a>Cadeau artikelen</a>
</nav>

<div class="page">
  <aside class="facets">
    <h3>Category</h3>
    <ul><li>Dirndl / Jurkjes</li><li class="active">Overige dameskleding</li></ul>
    <h3>Price</h3>
    <ul><li>Under € 5,00</li><li>Under € 15,00</li><li>Under € 25,00</li></ul>
    <h3>Size</h3>
    <ul><li>Small</li><li>Medium</li><li>Large</li><li>X-Large</li></ul>
  </aside>
  <main class="content">
    <div class="breadcrumb">Home / Tiroler Kleding / Triooise Dames / Overige dameskleding</div>
    <h1 class="title">Trioolse Dames</h1>
    <p class="intro">Alpenfeest.nl is the first shop specializing in Tyrolean articles. So if you have a Tyrolean party, or just looking for Tyrolean carnival clothes , you are guaranteed to come to the right place. Of course we also have everything for a great apres ski party in our range.</p>
    <div class="products">
      <article class="card"><div class="photo hat" role="img" aria-label="Green felt Tyrolean hat with feather"></div><div class="name">Hoed tiroler groen vilt</div><div class="row"><span class="price">€15,80</span><a class="buy">SHOP NOW</a></div></article>
      <article class="card"><div class="photo pants" role="img" aria-label="Beige Bavarian trousers with pink shirt"></div><div class="name">Bayernhose beige</div><div class="row"><span class="price">€ 13.50</span><a class="buy">SHOP NOW</a></div></article>
      <article class="card"><div class="photo wig" role="img" aria-label="Red braided wig costume"></div><div class="name">Gretchen Wig smooth</div><div class="row"><span class="price">€ 23.10</span><a class="buy">SHOP NOW</a></div></article>
      <article class="card"><div class="photo hat" role="img" aria-label="Green felt Tyrolean hat with feather"></div><div class="name">Hoed tiroler groen vilt</div><div class="row"><span class="price">€15,80</span><a class="buy">SHOP NOW</a></div></article>
      <article class="card"><div class="photo pants" role="img" aria-label="Beige Bavarian trousers with pink shirt"></div><div class="name">Bayernhose beige</div><div class="row"><span class="price">€ 13.50</span><a class="buy">SHOP NOW</a></div></article>
      <article class="card"><div class="photo wig" role="img" aria-label="Red braided wig costume"></div><div class="name">Gretchen Wig smooth</div><div class="row"><span class="price">€ 23.10</span><a class="buy">SHOP NOW</a></div></article>
      <article class="card"><div class="photo hat" role="img" aria-label="Green felt Tyrolean hat with feather"></div><div class="name">Hoed tiroler groen vilt</div><div class="row"><span class="price">€15,80</span><a class="buy">SHOP NOW</a></div></article>
      <article class="card"><div class="photo pants" role="img" aria-label="Beige Bavarian trousers with pink shirt"></div><div class="name">Bayernhose beige</div><div class="row"><span class="price">€ 13.50</span><a class="buy">SHOP NOW</a></div></article>
      <article class="card"><div class="photo wig" role="img" aria-label="Red braided wig costume"></div><div class="name">Gretchen Wig smooth</div><div class="row"><span class="price">€ 23.10</span><a class="buy">SHOP NOW</a></div></article>
    </div>
  </main>
</div>

<div class="banners">
  <div class="banner new"><div><h4>New!</h4><p>You would have to be half mad to dream me up.</p><a class="view">VIEW NOW</a></div><div class="art" role="img" aria-label="Child in Tyrolean costume"></div></div>
  <div class="banner hot"><div><h4>Hot!</h4><p>You would have to be half mad to dream me up.</p><a class="view">VIEW NOW</a></div><div class="art" role="img" aria-label="Crossed axes illustration"></div></div>
  <div class="banner sale"><div><h4>Sale!</h4><p>You would have to be half mad to dream me up.</p><a class="view">VIEW NOW</a></div><div class="art" role="img" aria-label="Woman in dirndl dress"></div></div>
</div>

<section class="signup">
  <h2>Sign up &amp; Save</h2>
  <p>Sign up for our newsletter now and be the first to know about sale offers and news exclusive to alpenfeest</p>
  <input value="Enter your email address">
  <button type="button">SIGN UP</button>
</section>

<footer class="footer">
  <section><h5>The Company</h5><ul><li>About Us</li><li>Contact</li><li>How to buy</li><li>FAQ's</li></ul></section>
  <section><h5>Customer Service</h5><ul><li>Need help? Give us a shout.</li><li>Customer hotline: 0861 555 0199</li><li>Return/refund policy</li></ul></section>
  <section><h5>Connect with us</h5><div class="social"><span></span><span></span><span></span><span></span><span></span></div></section>
</footer>
<div class="bottombar">
  Alpenfeest.nl | Bergweg 12 | 7500 AB ENSCHEDE | Alpenfeest.nl is onderdeel van Feestgroep BV.
  <div class="payments"><span></span><span></span><span></span><span></span><span class="wide"></span></div>
</div>
</body>
</html>
```